Harbo Hale - A non profit for healthy lifestyle and fitness within refugee camps

We need a logo and website design for a new 501c3 Non-Profit based in San Francisco called 'Harbo Hale'. We help coordinate trips across the globe to provide fitness classes to refugee camps to help refugees maintain a healthy lifestyle and fun while exercising.
Our first trip was to Greece and we hope to extend our reach by working with other non-profits to coordinate how we can help bring a healthy lifestyle and a wellness to refugees in need.
We would like to see website design that use the color green and blue. The final design should represent a welcoming website to encourage people to take a trip either by themselves, as a group, or with a corporate team.
We have 3 certified and experienced trainers that will be running these trips and with a hope of 20 volunteers per trip to help.

We are hoping to partner with another 501c3 called 'Tide to Dawn' which I have participated in and with the hopes of providing an easier and simpler user experience than their current website but with many of the same content.

We would like a 'Trips' page with previous trips, 'Trainers/Hosts' page with bios of the leaders hosting the event, 'Register Page' for folks to register for upcoming trips, 'About Us' page for our mission statement and work, 'Albums' page for photos taken on the trip, 'Contact Us' page for FAQs and questions to submit, and a 'Donate' page for people to donate to our cause.

I would like this page to be created in Word Press.

ie: http://www.tidetodawn-example.com.au/programs/

Target Market(s)

Volunteers, non-profit partners

Industry/Entity Type

Non-Profit

Number of Pages Required

4 page

Font styles to use
Sans Serif

Colors

Designer to choose colors to be used in the design.

Requirements
Must have
• 'Trips' page with previous trips, 'Trainers/Hosts' page with bios of the leaders hosting the event, 'Register Page' for folks to register for upcoming trips, 'About Us' page for our mission statement and work, 'Albums' page for photos taken on the trip, 'Contact Us' page for FAQs and questions to submit, and a 'Donate' page for people to donate to our cause.

```html
<!DOCTYPE html>
<html lang="en">
<head>
<meta charset="utf-8">
<title>Harbo Hale</title>
<link href="https://fonts.googleapis.com/css2?family=Open+Sans:wght@400;600;700;800&display=swap" rel="stylesheet">
<style>
:root{
  --dark:#333333;
  --green:#46b515;
  --orange:#f08a00;
  --blue:#1a6fb5;
  --text:#444444;
  --body:#555555;
  --band:#efefef;
  --white:#ffffff;
  --input:#eeeeee;
  --icon:#8a8a8a;
}
*{box-sizing:border-box;margin:0;padding:0}
html,body{width:1200px;height:2514px;overflow:hidden}
body{font-family:'Open Sans',Arial,sans-serif;color:var(--body);background:var(--white);position:relative}
.abs{position:absolute}
.btn{position:absolute;background:var(--green);color:var(--white);font-weight:700;font-size:14px;letter-spacing:.5px;display:flex;align-items:center;justify-content:center;width:151px;height:48px}
.more{color:var(--orange);font-weight:700;font-size:12.5px}
.photo{position:absolute}
.para{font-size:14.5px;line-height:25px;color:var(--body)}
h2.section{position:absolute;font-size:25px;font-weight:700;color:var(--text);letter-spacing:.5px}

/* top bar */
.topbar{left:0;top:0;width:1200px;height:69px;background:var(--dark)}
.brand{left:75px;top:20px;font-size:22px;font-weight:700;color:var(--white);letter-spacing:.5px}
.phone{left:830px;top:22px;color:var(--white);font-weight:700;font-size:15px;display:flex;align-items:center;gap:16px}
.donate{left:1017px;top:0;width:109px;height:69px;background:var(--green);color:var(--white);font-weight:700;font-size:12.5px;display:flex;align-items:center;justify-content:center}

/* nav */
.nav{left:0;top:69px;width:1200px;height:55px;background:var(--white)}
.nav a{position:absolute;top:21px;transform:translateX(-50%);font-size:13px;font-weight:700;color:#222;text-decoration:none;white-space:nowrap}
.nav a.active{color:var(--orange)}

/* hero */
.hero{left:0;top:124px;width:1200px;height:536px;background:linear-gradient(160deg,#244f8a 0%,#1f4b8c 40%,#2a5a96 70%,#1b3f74 100%)}
.hero-title{left:0;width:1200px;top:170px;text-align:center;color:var(--white);font-size:56px;font-weight:800;letter-spacing:1px}
.hero-sub{left:0;width:1200px;top:243px;text-align:center;color:var(--white);font-size:27px;font-weight:700;line-height:34px}
.dots{left:568px;top:498px;display:flex;gap:10px}
.dots span{width:10px;height:10px;border-radius:50%;background:var(--white)}
.dots span:first-child{background:var(--green)}

/* welcome */
.welcome h2{left:0;width:1200px;top:702px;text-align:center}
.welcome .para{position:absolute;left:80px;width:1040px;top:750px;text-align:center}

/* what we do */
.whatwedo{left:0;top:979px;width:1200px;height:493px;background:var(--band)}
.card{position:absolute;width:300px;height:189px;background:var(--white);padding:24px 28px}
.card h3{font-size:18px;font-weight:700;color:var(--blue);margin-bottom:4px}
.card p{font-size:13.5px;line-height:25px;margin-bottom:10px}

/* columns */
.col-img{top:1564px;width:330px;height:194px}
.col-text{top:1776px;width:330px}
.news-item{position:absolute;left:794px;width:330px}
.news-thumb{position:absolute;left:0;top:0;width:89px;height:89px}
.news-body{position:absolute;left:108px;top:-6px;width:208px}
.news-date{color:var(--blue);font-weight:700;font-size:13.5px}
.news-body p{font-size:13.5px;line-height:25px;margin-bottom:3px}

/* albums */
.albums{left:0;top:2028px;width:1200px;height:206px;background:var(--band)}
.arrow{width:22px;height:22px;border-radius:50%;background:#555;display:flex;align-items:center;justify-content:center}

/* footer */
.foot-h{font-size:13px;font-weight:700;color:var(--blue);letter-spacing:.3px}
.foot-list{font-size:14px;line-height:27.8px;color:var(--text)}
.field{position:absolute;left:615px;width:241px;height:41px;background:var(--input);font-size:13px;color:var(--text);padding:11px 14px}
.social{left:888px;top:2316px;display:flex;gap:16px}
.social span{width:18px;height:18px;background:var(--icon);border-radius:3px}
</style>
</head>
<body>

<header>
  <div class="abs topbar"></div>
  <div class="abs brand">HARBO HALE</div>
  <div class="abs phone">
    <svg width="14" height="14" viewBox="0 0 24 24"><path fill="#fff" d="M6.6 10.8a15.1 15.1 0 0 0 6.6 6.6l2.2-2.2c.3-.3.7-.4 1-.2 1.1.4 2.3.6 3.6.6.6 0 1 .4 1 1V20c0 .6-.4 1-1 1A17 17 0 0 1 3 4c0-.6.4-1 1-1h3.5c.6 0 1 .4 1 1 0 1.3.2 2.5.6 3.6.1.3 0 .7-.2 1z"/></svg>
    1-800-555-0142
  </div>
  <div class="abs donate">DONATE</div>
  <nav class="abs nav">
    <a class="active" style="left:168px">HOME</a>
    <a style="left:280px">ABOUT US</a>
    <a style="left:392px">TRIPS</a>
    <a style="left:528px">TRAINERS/ HOSTS</a>
    <a style="left:677px">REGISTER</a>
    <a style="left:796px">ALBUMS</a>
    <a style="left:895px">FAQ</a>
    <a style="left:1011px">CONTACT US</a>
  </nav>
</header>

<section class="abs hero" role="img" aria-label="People running an outdoor obstacle fitness course, blue-toned photo">
  <h1 class="abs hero-title">HARBO HALE</h1>
  <p class="abs hero-sub">We are a a new 501c3 Non-Profit based in San Francisco<br>&amp; non profit for healthy lifestyle and fitness within<br>refugee camps..</p>
  <div class="abs dots"><span></span><span></span><span></span><span></span></div>
</section>

<section class="welcome">
  <h2 class="section">WELCOME TO OUR WEBSITE</h2>
  <p class="para">Aliquam molestie, mi et imperdiet euismod, dui purus auctor tellus, et interdum lacus lectus et ante. Sed accumsan sollicitudin sapien, sit amet adipiscing turpis gravida ac. In congue, neque ac lobortis volutpat, libero mauris varius mi, vitae suscipit ipsum ligula vitae risus. Duis aliquam nibh a dui iaculis viverra id a velit. Vivamus egestas risus in magna varius commodo. Sed semper viverra egestas.<br>Etiam pretium porttitor lectus, vel ornare neque porta volutpat.</p>
  <div class="btn" style="left:525px;top:877px">READ MORE</div>
</section>

<section class="abs whatwedo">
  <h2 class="section" style="left:75px;top:80px">WHAT HARBO HALE DO</h2>
  <p class="para abs" style="left:75px;top:126px;width:410px">Aliquam molestie, mi et imperdiet euismod, dui purus auctor tellus, et interdum lacus lectus et ante.<br>Sed accumsan sollicitudin sapien, sit amet adipiscing turpis gravida ac. In congue, neque ac lobortis volutpat, libero mauris varius mi, vitae suscipit ipsum ligula vitae risus. Duis aliquam nibh a dui iaculis viverra id a velit. Vivamus egestas risus in magna varius commodo.<br>Sed semper viverra egestas.</p>
  <div class="btn" style="left:75px;top:357px">READ MORE</div>

  <div class="photo" style="left:526px;top:57px;width:300px;height:189px;background:linear-gradient(180deg,#9fc0e6 0%,#c9d3dc 45%,#b3a99a 100%)" role="img" aria-label="Children playing among white tents in a refugee camp"></div>
  <div class="card" style="left:826px;top:57px">
    <h3>REFUGEE FITNESS CAMPS</h3>
    <p>Aliquam molestie, mi et imperdiet euismod, dui purus auctor tellus, et interdum lacus lectus et ante.</p>
    <div class="more">READ MORE</div>
  </div>
  <div class="card" style="left:526px;top:246px">
    <h3>EXERCISE SESSIONS</h3>
    <p>Aliquam molestie, mi et imperdiet euismod, dui purus auctor tellus, et interdum lacus lectus et ante.</p>
    <div class="more">READ MORE</div>
  </div>
  <div class="photo" style="left:826px;top:246px;width:300px;height:189px;background:linear-gradient(180deg,#8f8f8f 0%,#5c5c5c 60%,#2e2e2e 100%)" role="img" aria-label="Group portrait of the trainer team in an indoor room"></div>
</section>

<section>
  <h2 class="section" style="left:75px;top:1510px">TRIPS</h2>
  <div class="photo col-img" style="left:75px;background:linear-gradient(180deg,#7aa64a 0%,#5f8f34 50%,#4c7a2a 100%)" role="img" aria-label="Runners in a race on a grassy path"></div>
  <p class="para abs col-text" style="left:75px">Aliquam molestie, mi et imperdiet euismod, dui purus auctor tellus, et interdum lacus lectus et ante.&nbsp; Sed accumsan sollicitudin sapien, sit amet adipiscing turpis neque ac lobortis volutpat..</p>
  <div class="btn" style="left:75px;top:1927px">READ MORE</div>

  <h2 class="section" style="left:434px;top:1510px">TRAINERS/ HOSTS</h2>
  <div class="photo col-img" style="left:434px;background:linear-gradient(180deg,#3a3a3a 0%,#7a6a60 50%,#d8d8d8 100%)" role="img" aria-label="Portrait of a smiling fitness trainer with a whistle"></div>
  <p class="para abs col-text" style="left:434px">Aliquam molestie, mi et imperdiet euismod, dui purus auctor tellus, et interdum lacus lectus et ante.&nbsp; Sed accumsan sollicitudin sapien, sit amet adipiscing turpis neque ac lobortis volutpat..</p>
  <div class="btn" style="left:434px;top:1927px">READ MORE</div>

  <h2 class="section" style="left:792px;top:1510px">NEWS UPDATES</h2>
  <div class="news-item" style="top:1565px">
    <div class="news-thumb" style="background:linear-gradient(180deg,#9db6cf,#6d5a55)" role="img" aria-label="Refugee family walking"></div>
    <div class="news-body"><div class="news-date">AUG 02, 2017</div><p>Aliquam molestie, mi et<br>imperdiet euismod, dui purus</p><div class="more">READ MORE</div></div>
  </div>
  <div class="news-item" style="top:1679px">
    <div class="news-thumb" style="background:linear-gradient(180deg,#4f7fc0,#3b3b3b)" role="img" aria-label="Volunteers helping people ashore"></div>
    <div class="news-body"><div class="news-date">AUG 02, 2017</div><p>Aliquam molestie, mi et<br>imperdiet euismod, dui purus</p><div class="more">READ MORE</div></div>
  </div>
  <div class="news-item" style="top:1793px">
    <div class="news-thumb" style="background:linear-gradient(180deg,#b9c6d3,#5f5a55)" role="img" aria-label="Crowd at a refugee camp"></div>
    <div class="news-body"><div class="news-date">AUG 02, 2017</div><p>Aliquam molestie, mi et<br>imperdiet euismod, dui purus</p><div class="more">READ MORE</div></div>
  </div>
  <div class="btn" style="left:793px;top:1927px">READ MORE</div>
</section>

<section class="abs albums">
  <h2 class="section" style="left:75px;top:62px">ALBUMS</h2>
  <div class="abs" style="left:75px;top:111px;display:flex;gap:8px">
    <div class="arrow"><svg width="10" height="10" viewBox="0 0 10 10"><path d="M6.5 1.5 3 5l3.5 3.5" fill="none" stroke="#fff" stroke-width="2"/></svg></div>
    <div class="arrow"><svg width="10" height="10" viewBox="0 0 10 10"><path d="M3.5 1.5 7 5 3.5 8.5" fill="none" stroke="#fff" stroke-width="2"/></svg></div>
  </div>
  <div class="photo" style="left:255px;top:32px;width:280px;height:141px;background:linear-gradient(180deg,#a9bfd4 0%,#8c8378 60%,#6b6258 100%)" role="img" aria-label="Refugees walking along a road"></div>
  <div class="photo" style="left:551px;top:32px;width:280px;height:141px;background:linear-gradient(180deg,#4f86cc 0%,#6f8fb0 50%,#3e3e40 100%)" role="img" aria-label="Rescue volunteers on a shoreline"></div>
  <div class="photo" style="left:846px;top:32px;width:280px;height:141px;background:linear-gradient(180deg,#bccbd9 0%,#8f8b86 60%,#4e4a46 100%)" role="img" aria-label="Line of people at a border crossing"></div>
</section>

<footer>
  <div class="abs foot-h" style="left:75px;top:2280px">SITE MAP</div>
  <div class="abs foot-list" style="left:75px;top:2302px">Home<br>About us<br>Trips<br>Trainers/ Hosts<br>Register<br>Albums</div>
  <div class="abs foot-list" style="left:228px;top:2302px">Donate<br>FAQ<br>Contact us</div>

  <div class="abs foot-h" style="left:345px;top:2280px">CONTACT INFO</div>
  <div class="abs" style="left:345px;top:2304px;font-size:13px;font-weight:700;color:var(--orange)">HARBO HALE</div>
  <div class="abs foot-list" style="left:345px;top:2330px;width:220px;line-height:24px">4120 Alder Lane<br>Kelbridge, KB7 2QX</div>
  <div class="abs foot-list" style="left:345px;top:2386px;line-height:28px">
    <div style="display:flex;align-items:center;gap:18px"><svg width="12" height="12" viewBox="0 0 24 24"><path fill="#444" d="M6.6 10.8a15.1 15.1 0 0 0 6.6 6.6l2.2-2.2c.3-.3.7-.4 1-.2 1.1.4 2.3.6 3.6.6.6 0 1 .4 1 1V20c0 .6-.4 1-1 1A17 17 0 0 1 3 4c0-.6.4-1 1-1h3.5c.6 0 1 .4 1 1 0 1.3.2 2.5.6 3.6.1.3 0 .7-.2 1z"/></svg>1-800-555-0142</div>
    <div style="display:flex;align-items:center;gap:18px"><svg width="12" height="12" viewBox="0 0 24 24"><path fill="#444" d="M2 5h20v14H2z"/><path d="M2 5l10 8 10-8" fill="none" stroke="#fff" stroke-width="2"/></svg>info@harbohale-example.org</div>
    <div style="display:flex;align-items:center;gap:18px"><svg width="12" height="12" viewBox="0 0 24 24"><path fill="#444" d="M12 2a7 7 0 0 0-7 7c0 5 7 13 7 13s7-8 7-13a7 7 0 0 0-7-7zm0 9.5A2.5 2.5 0 1 1 12 6.5a2.5 2.5 0 0 1 0 5z"/></svg>Map Direction</div>
  </div>

  <div class="abs foot-h" style="left:615px;top:2280px">EMAIL SIGN UP</div>
  <div class="field" style="top:2318px">Enter Name</div>
  <div class="field" style="top:2368px">Enter Email Address</div>
  <div class="btn" style="left:766px;top:2417px;width:90px;height:38px;font-size:12.5px">SIGN UP</div>

  <div class="abs foot-h" style="left:888px;top:2280px">FOLLOW US</div>
  <div class="abs social"><span></span><span></span><span></span><span></span><span></span></div>
  <div class="abs" style="left:888px;top:2420px;font-size:12px;line-height:21px;color:var(--text)">Copyright © 2017. Company Name<br>All Right Reserved</div>
</footer>

</body>
</html>
```